Business cards and letterhead
UK size business cards/letterhead
Project: Business cards and letterhead
Business cards and letterhead - Information Technology
Creative Brief
Professional
Gareth Pellow
Director
148 Ashcombe Lane Twickenham Middlesex TW4 3QR
gareth.pellow@corvalisen.com
www.corvalisen.com
Note business card needs to be UK-sized (i.e. 85 x 55)/double sided, and the letterhead suitable for A4 paper Back of card can contain some/all of suggested text, depending upon how well it fits
ECM Consultancy Services - Project Management and Delivery - Implementation Planning - Data Conversion Management - Existing System Reviews - Software Design and Development - Test Strategy Definition and Execution

```html
<!DOCTYPE html>
<html lang="en">
<head>
<meta charset="utf-8">
<title>Corvalisen business card</title>
<link rel="stylesheet" href="https://fonts.googleapis.com/css2?family=Arimo:wght@400;700&display=swap">
<style>
  :root {
    --backdrop: #e8e4de;
    --card: #ffffff;
    --band-dark: #0f6f93;
    --band-mid: #1a8bb5;
    --band-light: #5fb6d6;
    --ink: #262a2e;
    --accent: #1d7fae;
    --muted: #6d7379;
    --rule: #b8bec4;
    --icon: #2b6f92;
  }
  * { margin: 0; padding: 0; box-sizing: border-box; }
  html, body {
    width: 1200px; height: 780px; overflow: hidden;
    background: var(--backdrop);
    font-family: "Arimo", Arial, sans-serif;
  }
  .card {
    position: absolute; left: 90px; top: 60px;
    width: 1020px; height: 660px;
    background: var(--card);
    border-radius: 42px;
    box-shadow: 0 6px 22px rgba(0,0,0,0.18);
    overflow: hidden;
  }
  .band {
    position: absolute; left: 0; right: 0; top: 112px; height: 128px;
    background: linear-gradient(180deg, var(--band-mid) 0%, var(--band-dark) 100%);
  }
  .band::before {
    content: ""; position: absolute; left: 0; right: 0; top: 0; height: 10px;
    background: var(--band-light);
  }
  .brand-mark {
    position: absolute; left: 50%; top: 82px;
    width: 120px; height: 120px; margin-left: -60px;
    border-radius: 50%;
    background: var(--ink);
    border: 6px solid var(--card);
  }
  .brand-name {
    position: absolute; left: 0; right: 0; top: 250px;
    text-align: center;
    font-weight: 700; font-size: 66px; letter-spacing: 2px;
    color: var(--ink);
  }
  .person {
    position: absolute; right: 530px; top: 420px;
    text-align: right; color: var(--muted);
    font-size: 23px; line-height: 1.4;
  }
  .person-name { color: var(--accent); font-size: 32px; line-height: 1.2; }
  .person-role { margin-bottom: 18px; }
  .divider {
    position: absolute; left: 520px; top: 418px;
    width: 2px; height: 178px; background: var(--rule);
  }
  .contacts {
    position: absolute; left: 548px; top: 424px;
    list-style: none; color: var(--muted); font-size: 23px;
  }
  .contacts li { display: flex; align-items: center; height: 46px; }
  .contacts svg { width: 28px; height: 28px; margin-right: 14px; fill: var(--icon); }
</style>
</head>
<body>
  <main class="card">
    <div class="band"></div>
    <div class="brand-mark"></div>
    <div class="brand-name">CORVALISEN</div>

    <section class="person">
      <div class="person-name">Gareth Pellow</div>
      <div class="person-role">Director</div>
      <div>148 Ashcombe Lane, Twickenham</div>
      <div>Middlesex, TW4 3QR</div>
    </section>

    <div class="divider"></div>

    <ul class="contacts">
      <li>
        <svg viewBox="0 0 24 24" aria-hidden="true"><path d="M6.6 10.8a15 15 0 0 0 6.6 6.6l2.2-2.2c.3-.3.7-.4 1-.2 1.1.4 2.3.6 3.6.6.6 0 1 .4 1 1V20c0 .6-.4 1-1 1A17 17 0 0 1 3 4c0-.6.4-1 1-1h3.5c.6 0 1 .4 1 1 0 1.3.2 2.5.6 3.6.1.3 0 .7-.2 1z"/></svg>
        +44-7700-900-418
      </li>
      <li>
        <svg viewBox="0 0 24 24" aria-hidden="true"><path d="M3 5h18c.6 0 1 .4 1 1v12c0 .6-.4 1-1 1H3c-.6 0-1-.4-1-1V6c0-.6.4-1 1-1zm1 2.3V17h16V7.3l-8 5.2z M4.8 7 12 11.6 19.2 7z"/></svg>
        gareth.pellow@corvalisen.com
      </li>
      <li>
        <svg viewBox="0 0 24 24" aria-hidden="true"><path d="M12 2a10 10 0 1 0 0 20 10 10 0 0 0 0-20zm6.9 9h-3a15 15 0 0 0-1.2-5.6A8 8 0 0 1 18.9 11zM12 4.1c.9 1.2 1.8 3.6 1.9 6.9h-3.8c.1-3.3 1-5.7 1.9-6.9zM9.3 5.4A15 15 0 0 0 8.1 11h-3a8 8 0 0 1 4.2-5.6zM5.1 13h3a15 15 0 0 0 1.2 5.6A8 8 0 0 1 5.1 13zm6.9 6.9c-.9-1.2-1.8-3.6-1.9-6.9h3.8c-.1 3.3-1 5.7-1.9 6.9zm2.7-1.3a15 15 0 0 0 1.2-5.6h3a8 8 0 0 1-4.2 5.6z"/></svg>
        www.corvalisen.com
      </li>
    </ul>
  </main>
</body>
</html>
```